Lantren Grove Days introduciendo Quillaro.example

We need the name of the event look like a trade mark. for other activities or events.
"Lantern Grove Days" the part of introducing quillaro could be lower so people only can relate to that.

We need a flyer design for an event is a Bazar where our principal comunication target are the consumer but stores will be atracted to it with this same flyer.....

the graphic disign could be abstract clean backgrown more focus on the name of the event. information font is not what we want to predominate on this. is more about some modern and elegant disign.

We need a flyer design for an event is a Bazar where our stores and customer will interact eachother, this day people will know more about what is quillaro for the dominican republic market, its like the firts zentrova local where individuals and businesses can sell products anywhere in de country. but this quillaro in our comunication is secundary.......we need people focus o the Bazar. the Logo of quillaro could be there small.

This event have the purpuse to atract both target our stores vendors and the general public where they can enjoy a nice sunday shopping day from 11am to 10pm, this event will take place indoor and outdoor location where the offices of quillaro are,. its a mall where inside the offices we will have many stores selling as well outside, djs playin live and food placements where clients can rest and enjoy the day.

We name this Bazaar Lantern Grove Days introducing quillaro because we want to take this event to diferents cities to afiliate stores in to this new plataform so they can open there stores online with us and at the same time promote the site with the whole country as a marketing effort.

Target Market(s)

Young adult between 18 and 35

Industry/Entity Type

Marketing

Font styles to use
Serif

Requirements
Must have
• Fresh and modern look.

```html
<!DOCTYPE html>
<html lang="es">
<head>
<meta charset="utf-8">
<title>Lantern Grove Days — Flyer</title>
<link href="https://fonts.googleapis.com/css2?family=Anton&family=Questrial&family=Yellowtail&display=swap" rel="stylesheet">
<style>
  :root {
    --stage: #2f2521;
    --orange: #f7a53a;
    --brown: #4e2a27;
    --white: #ffffff;
    --shadow: rgba(120, 70, 20, 0.45);
  }
  * { margin: 0; padding: 0; box-sizing: border-box; }
  html, body {
    width: 967px; height: 1200px; overflow: hidden;
    background: var(--stage);
  }
  .flyer {
    position: absolute; left: 70px; top: 15px;
    width: 689px; height: 975px;
    background: var(--orange);
    transform: scale(1.2); transform-origin: 0 0;
    font-family: "Questrial", sans-serif;
    text-align: center;
    overflow: hidden;
  }
  .brand {
    position: absolute; left: 251px; top: 56px;
    width: 187px; height: 38px;
    background: var(--white);
    display: flex; align-items: center; justify-content: center; gap: 8px;
    color: var(--orange); font-size: 20px;
  }
  .brand__mark { width: 16px; height: 16px; background: var(--orange); }
  .bag-shadow {
    position: absolute; left: 90px; top: 540px;
    width: 520px; height: 110px;
    background: radial-gradient(ellipse at center, var(--shadow) 0%, transparent 70%);
  }
  .bag {
    position: absolute; left: 0; top: 0; width: 689px; height: 700px;
  }
  .event-title {
    position: absolute; left: 200px; top: 280px; width: 330px;
    transform: rotate(-4deg);
    font-family: "Anton", sans-serif; color: var(--white);
    line-height: 0.92; text-transform: uppercase; letter-spacing: 0;
  }
  .event-title span { display: block; }
  .event-title .l1 { font-size: 76px; }
  .event-title .l2 { font-size: 108px; }
  .event-title .l3 { font-size: 128px; }
  .date {
    position: absolute; top: 669px; left: 0; right: 0;
    color: var(--white); font-size: 14px;
  }
  .tagline {
    position: absolute; top: 704px; left: 0; right: 0;
    font-family: "Yellowtail", cursive; color: var(--brown); font-size: 40px;
  }
  .tagline-es {
    position: absolute; top: 770px; left: 0; right: 0;
    color: var(--white); font-size: 15px;
  }
  .guest-label {
    position: absolute; top: 801px; left: 0; right: 0;
    color: var(--brown); font-size: 16px;
  }
  .guest-name {
    position: absolute; top: 823px; left: 0; right: 0;
    color: var(--brown); font-size: 32px;
  }
  .happy-hour {
    position: absolute; top: 867px; left: 0; right: 0;
    color: var(--brown); font-size: 15px;
  }
  .details {
    position: absolute; left: 0; right: 0; top: 893px; height: 82px;
    background: var(--brown); color: var(--white);
    font-size: 19px; line-height: 30px; padding-top: 9px;
  }
</style>
</head>
<body>
  <main class="flyer">
    <div class="brand"><span class="brand__mark"></span><span>quillaro</span></div>

    <div class="bag-shadow"></div>
    <svg class="bag" viewBox="0 0 689 700" role="img" aria-label="Shopping bag illustration in dark brown holding the event name">
      <polygon points="186,281 501,276 533,588 153,633" fill="var(--brown)"/>
    </svg>

    <h1 class="event-title">
      <span class="l1">Lantern</span>
      <span class="l2">Grove</span>
      <span class="l3">Days</span>
    </h1>

    <p class="date">DOMINGO 30 NOVIEMBRE</p>
    <p class="tagline">Join us and enjoy a diferent way to buy!</p>
    <p class="tagline-es">Acompañanos y disfruta de una manera diferente de comprar!!</p>
    <p class="guest-label">Invitado especial</p>
    <p class="guest-name">DJ CORVEL</p>
    <p class="happy-hour">Happy hour desde las 4:30pm</p>

    <div class="details">
      <p>Hora: desde 11am a 10pm</p>
      <p>Donde: Plaza Almendra, Ave. Las Brisas esq. Colinas.</p>
    </div>
  </main>
</body>
</html>
```